BrightPath Dental
Web Presence
BrightPath Dental - Information Technology
Creative Brief
Information Technology
www.brightpathdental-demo.com
Brightpath Dental provides a wide variety of high tech dental solutions at a competitive price. We pride ourselves on the extremely high level and speed of service that we provide to our clientele. We are a local computer company that specializes in bringing our clientele the best dental technology solutions available. By allowing us to correctly integrate the right dental technology solutions, it gives your practice a technological competitive edge, increases production, and significantly enhances your patient’s experience. We provide a full array of computer services for both small and large practices. Our team services PC's and networks, digital x-ray / imaging equipment, we also provide software & hardware sales, service, upgrades, and installations, as well as data storage and backup solutions. We also provide ongoing technical support to keep you comfortable with changing technologies and ensure your practice productivity.
would like CMS designed website for either joomla or wordpress. We need the wording and the design -- we are a Lumoverde Reseller and Installer so please check out their site listed below. our logo is available: http://orders.markcraftstudio-demo.com/contests/business-logo-brightpathdental
left side
http://www.lumoverdedental-demo.com/us_region/index.aspx
http://www.qwbadvisors-demo.com/articles
http://www.orb-sys-demo.com/index.html
Additional Sites that do similar work: http://www.mnzerodental-demo.com/dataprotection.htm http://www.fenwro-demo.com/customer_care.html http://www.glimvo-demo.com/ http://www.mnzerodental-demo.com/dataprotection.htm

```html
<!DOCTYPE html>
<html lang="en">
<head>
<meta charset="utf-8">
<title>BrightPath Dental – Customer Care</title>
<link rel="stylesheet" href="https://fonts.googleapis.com/css2?family=Arimo:wght@400;700&display=swap">
<style>
  :root{
    --page:#ffffff;
    --panel:#e4e5e7;
    --blue:#1f63b4;
    --blue-dark:#0f4a8e;
    --blue-light:#5b97d8;
    --red:#b3141b;
    --ink:#111111;
    --muted:#6f6f6f;
    --nav-text:#ffffff;
  }
  *{box-sizing:border-box;margin:0;padding:0}
  html,body{width:1200px;height:912px;overflow:hidden;background:var(--page)}
  body{position:relative;font-family:"Arimo",Arial,sans-serif;color:var(--ink)}

  .brand{position:absolute;left:195px;top:30px;display:flex;align-items:center;gap:12px}
  .brand-dot{width:40px;height:40px;border-radius:50%;background:var(--blue)}
  .brand-name{font-size:30px;font-weight:700;color:var(--blue)}

  .utility-links{position:absolute;left:745px;top:16px;font-size:19px;color:#444;letter-spacing:.5px;word-spacing:6px}
  .search{position:absolute;left:825px;top:62px;display:flex;align-items:center;gap:10px}
  .search label{font-size:19px;font-weight:700;color:#333}
  .search-box{width:140px;height:26px;border:1px solid #9a9a9a;background:#fff}

  .panel{position:absolute;left:145px;top:120px;width:923px;height:742px;background:var(--panel)}

  .main-nav{position:absolute;left:145px;top:120px;width:205px}
  .main-nav a{display:block;height:43px;margin-bottom:2px;line-height:43px;text-align:center;
    color:var(--nav-text);font-weight:700;font-size:18px;text-decoration:none;
    background:linear-gradient(#4d8bd3,var(--blue) 55%,#1a55a0);
    border-bottom:2px solid #9ec0e8}
  .nav-tail{display:block;margin-top:-2px}

  .hero{position:absolute;left:350px;top:120px;width:482px;height:325px;
    background:linear-gradient(120deg,#b9c7d6 0%,#e6edf3 35%,#8fa3b8 65%,#4f6478 100%)}

  .contact-card{position:absolute;left:838px;top:150px;width:217px;height:262px;border-radius:8px;
    background:linear-gradient(#ffffff 0%,#f3f3f3 50%,#d9d9d9 100%);text-align:center}
  .contact-card h2{margin-top:18px;font-size:31px;font-weight:700;color:#000}
  .phone{display:inline-block;margin-top:14px;padding:9px 16px;border-radius:24px;
    background:linear-gradient(#d3262c,var(--red));color:#fff;font-weight:700;font-size:23px}
  .hours{margin-top:22px;color:var(--muted);font-weight:700;font-size:25px;line-height:1.3}

  .intro{position:absolute;left:350px;top:455px;width:680px;font-size:17.5px;line-height:1.28}
  .intro p+p{margin-top:6px}
  .intro strong{color:var(--blue);font-weight:700}

  .service{position:absolute;top:595px;text-align:center}
  .service-tab{display:block;height:38px;line-height:36px;border-radius:6px;
    background:linear-gradient(#5a97d9,var(--blue));color:#fff;font-weight:700;font-size:14px;
    border-bottom:2px solid #9ec0e8}
  .service-photo{display:block;margin-top:22px;height:127px}
  .service p{margin-top:8px;font-size:9px;line-height:1.3;text-align:left;color:#333}
  .dentists{left:345px;width:160px}
  .dentists .service-photo{background:linear-gradient(135deg,#6fa8d8,#e7d6c8 55%,#8fb7de)}
  .ortho{left:595px;width:190px}
  .ortho .service-tab{width:160px;margin:0 auto}
  .ortho .service-photo{background:linear-gradient(135deg,#e9eef2,#f8f8f8 50%,#b7c6d2)}
  .surgeons{left:858px;width:192px}
  .surgeons .service-tab{line-height:16px;padding-top:3px;font-size:13px}
  .surgeons .service-photo{background:linear-gradient(135deg,#2d5466,#5d8f94 50%,#1e3a46)}

  .social{position:absolute;left:165px;top:825px;display:flex;gap:7px}
  .social span{width:22px;height:22px;border-radius:3px;background:var(--blue-dark)}
  .social span.wide{width:52px;background:#b3141b}

  .site-footer{position:absolute;left:145px;top:862px;width:923px;height:50px;
    background:var(--blue);color:#fff;font-size:12px;font-weight:700;text-align:center;line-height:50px}
</style>
</head>
<body>
  <header>
    <div class="brand"><span class="brand-dot"></span><span class="brand-name">BrightPath Dental</span></div>
    <nav class="utility-links">EMAIL | BLOG | NEWSLETTER</nav>
    <div class="search"><label>Search</label><span class="search-box"></span></div>
  </header>

  <div class="panel"></div>

  <nav class="main-nav">
    <a href="#">HOME</a>
    <a href="#">OUR GALLERY</a>
    <a href="#">YOUR EXPERTS</a>
    <a href="#">ABOUT US</a>
    <a href="#">CUSTOMER CARE</a>
    <a href="#">PARTNERS</a>
    <a href="#">CONTACT US</a>
    <svg class="nav-tail" width="205" height="30" viewBox="0 0 205 30" aria-hidden="true">
      <path d="M0 0 H205 V8 Q120 30 40 26 Q12 24 0 14 Z" fill="#1f63b4"/>
    </svg>
  </nav>

  <div class="hero" role="img" aria-label="Modern dental treatment room with chair and overhead lamp"></div>

  <aside class="contact-card">
    <h2>Contact Us</h2>
    <div class="phone">888-555-0142</div>
    <div class="hours">Monday&nbsp; - &nbsp;Friday<br>9 :00 am &nbsp;- &nbsp;6 :00 pm</div>
  </aside>

  <section class="intro">
    <p>Our Customer Care Center team comes to the office everyday prepared and ready to keep our clients' practices running smoothly, seamlessly and stress-free.</p>
    <p><strong>On-site Service -</strong> Our support team is committed to being responsive to you, if and when you need us. We work to expedite your requests and schedule service to be as unobtrusive to your patients and practice as possible. Hourly rate.</p>
  </section>

  <article class="service dentists">
    <span class="service-tab">Dentists</span>
    <div class="service-photo" role="img" aria-label="Dentist treating a patient"></div>
    <p>Our team helps you use today's computer and digital tools to strengthen your dental practice.</p>
  </article>

  <article class="service ortho">
    <span class="service-tab">Orthodontists</span>
    <div class="service-photo" role="img" aria-label="Orthodontist with a young patient"></div>
    <p>We have the skills and experience to keep your practice on the cutting edge of orthodontic tech.</p>
  </article>

  <article class="service surgeons">
    <span class="service-tab">Oral &amp; Maxillofacial<br>Surgeons</span>
    <div class="service-photo" role="img" aria-label="Surgical team in an operating room"></div>
    <p>Work with a team that understands the unique needs of an OMS practice, from records to 3D imaging.</p>
  </article>

  <div class="social" aria-label="Social links"><span></span><span></span><span class="wide"></span></div>

  <footer class="site-footer">Copyright © 2010 &nbsp;- &nbsp;All rights reserved.</footer>
</body>
</html>
```